Flyer Design

Company name Glimbra, ecofriendly oven cleaning. See website glimbra-example.co.uk. Looking for a flyer to offer a 10% discount off web prices Picture of shiny oven, highlighting eco aspect

Industry/Entity Type

It Company

```html
<!DOCTYPE html>
<html lang="en">
<head>
<meta charset="utf-8">
<title>Glimbra – 10% off flyer</title>
<link rel="stylesheet" href="https://fonts.googleapis.com/css2?family=Arimo:wght@700&family=Crimson+Text:wght@600&family=Roboto+Condensed:wght@400&family=Source+Sans+3:ital,wght@1,700&display=swap">
<style>
  :root {
    --backdrop: #141414;
    --paper: #ffffff;
    --green: #3f9c3f;
    --green-light: #b3d47a;
    --kitchen-dark: #3f3632;
    --kitchen-light: #a69d95;
    --blue-dark: #2a3f8c;
    --blue-light: #8f9fd8;
    --steel-light: #e4e6e8;
    --steel-dark: #1c1d20;
  }
  * { margin: 0; padding: 0; box-sizing: border-box; }
  html, body {
    width: 1200px; height: 1200px; overflow: hidden;
    background: var(--backdrop);
  }
  .flyer {
    position: absolute; left: 62px; top: 220px;
    width: 1076px; height: 762px;
    background: var(--paper);
    overflow: hidden;
  }
  .header-photo {
    position: absolute; left: 0; top: 0; width: 100%; height: 214px;
    background: linear-gradient(100deg, var(--kitchen-dark) 0%, #6a5c52 45%, var(--kitchen-light) 100%);
  }
  .brand-name {
    position: absolute; left: 244px; top: 30px;
    font-family: "Arimo", Arial, sans-serif; font-weight: 700;
    font-size: 124px; line-height: 1; letter-spacing: -2px;
    color: var(--green);
  }
  .brand-tagline {
    position: absolute; left: 248px; top: 155px;
    font-family: "Arimo", Arial, sans-serif; font-weight: 700;
    font-size: 40px; line-height: 1;
    color: var(--green-light);
  }
  .headline {
    position: absolute; left: 0; top: 222px; width: 100%;
    text-align: center; padding-left: 24px;
    font-family: "Source Sans 3", "Myriad Pro", sans-serif;
    font-style: italic; font-weight: 700;
    font-size: 50px; line-height: 1; letter-spacing: 1px;
    color: var(--green);
  }
  .offer-get {
    position: absolute; left: 204px; top: 330px;
    font-family: "Roboto Condensed", sans-serif; font-weight: 400;
    font-size: 96px; line-height: 1; letter-spacing: -2px;
    color: var(--green);
  }
  .offer-amount {
    position: absolute; left: 310px; top: 250px;
    font-family: "Crimson Text", Georgia, serif; font-weight: 600;
    font-size: 280px; line-height: 1; letter-spacing: -6px;
    color: var(--green);
  }
  .offer-terms {
    position: absolute; left: 0; top: 492px; width: 100%;
    text-align: center; padding-left: 70px;
    font-family: "Roboto Condensed", sans-serif; font-weight: 400;
    font-size: 42px; line-height: 1; letter-spacing: -0.5px;
    color: var(--green);
  }
  .kitchen-photo {
    position: absolute; left: 0; top: 546px; width: 584px; height: 216px;
    background: linear-gradient(120deg, var(--blue-dark) 0%, #5566b8 50%, var(--blue-light) 100%);
  }
  .oven-photo {
    position: absolute; left: 584px; top: 546px; width: 492px; height: 216px;
    background: linear-gradient(180deg, var(--steel-light) 0%, #c9cccf 30%, #5a5d62 55%, var(--steel-dark) 100%);
  }
</style>
</head>
<body>
  <main class="flyer">
    <div class="header-photo" role="img" aria-label="Photo of a modern kitchen interior in warm brown tones"></div>
    <div class="brand-name">glimbra</div>
    <div class="brand-tagline">eco-friendly oven cleaning</div>

    <p class="headline">Give your oven a great new look!</p>
    <div class="offer-get">get</div>
    <div class="offer-amount">10%</div>
    <p class="offer-terms">off web prices at glimbra-example.co.uk</p>

    <div class="kitchen-photo" role="img" aria-label="Photo of a blue kitchen with steel pots on a hob and a sink"></div>
    <div class="oven-photo" role="img" aria-label="Photo of a shiny stainless steel oven door and handle"></div>
  </main>
</body>
</html>
```